Concrete Construction Business Card design

We are a commercial concrete construction company based in Texas. a family owned business which our trade was passed down and taught by our grandfather whom we want represented in this design. our grandfathers nick name was "pepe" so we are wanting the letter G to be symbolized in some way with a red pepe . colors should be possibly a grey color back ground , green letter g and red pepe pepper , to be left for you to decide with integrity , concrete professionalism,and mexican heritage

Target Market(s)

general contractors, architects,inverstors, and engineers

Industry/Entity Type

Concrete

Contact Information for Business Card

Herrera Concrete Construction LLC, Ramiro Herrera, 1872 Bramblewood Ln. Denton, TX 76209, (940)318-2746, rhslabworkllc48@quarrymail.net

```html
<!DOCTYPE html>
<html lang="en">
<head>
<meta charset="utf-8">
<title>Herrera Concrete Construction LLC – Business Card</title>
<link href="https://fonts.googleapis.com/css2?family=Tinos:wght@400;700&family=Arimo:wght@400;700&display=swap" rel="stylesheet">
<style>
  :root {
    --stage: #000000;
    --card: #707070;
    --card-edge: #8a8a8a;
    --ink: #ffffff;
    --divider: #a0a0a0;
    --accent-green: #3ab54a;
  }
  html, body {
    margin: 0;
    padding: 0;
    width: 1200px;
    height: 1000px;
    overflow: hidden;
    background: var(--stage);
  }
  .business-card {
    position: absolute;
    left: 283px;
    top: 314px;
    width: 634px;
    height: 372px;
    box-sizing: border-box;
    background: var(--card);
    border: 1px solid var(--card-edge);
  }
  .brand-dot {
    position: absolute;
    left: 140px;
    top: 105px;
    width: 56px;
    height: 56px;
    border-radius: 50%;
    background: var(--accent-green);
  }
  .brand-name {
    position: absolute;
    left: 227px;
    top: 114px;
    font-family: "Tinos", "Times New Roman", serif;
    font-weight: 700;
    color: var(--ink);
    line-height: 1;
    white-space: nowrap;
  }
  .brand-name .family {
    display: block;
    font-size: 38px;
  }
  .brand-name .trade {
    display: block;
    font-size: 22px;
    margin-top: 4px;
  }
  .contact {
    position: absolute;
    left: 274px;
    top: 237px;
    height: 84px;
    padding-left: 21px;
    border-left: 1px solid var(--divider);
    font-family: "Arimo", Arial, sans-serif;
    color: var(--ink);
    white-space: nowrap;
  }
  .contact-name {
    margin: 2px 0 11px;
    font-size: 14px;
    font-weight: 700;
  }
  .contact-details {
    margin: 0;
    font-size: 14px;
    font-weight: 400;
    line-height: 17px;
  }
</style>
</head>
<body>
  <div class="business-card">
    <span class="brand-dot" aria-hidden="true"></span>
    <div class="brand-name">
      <span class="family">Herrera</span>
      <span class="trade">Concrete Construction LLC</span>
    </div>
    <div class="contact">
      <p class="contact-name">Ramiro Herrera</p>
      <p class="contact-details">
        1872 Bramblewood Ln. Denton, TX 76209,<br>
        (940) 318-2746,<br>
        rhslabworkllc48@quarrymail.net
      </p>
    </div>
  </div>
</body>
</html>
```